Business Card Design

Velvet Pixel Promotions

An online marketing consulting & strategy business for the cosmetic niche

We specialise in Increasing Leads, Conversions & Content Marketing

I am looking for a very clean, BOLD business card that is simple & effective

Target Market(s)

cosmetic surgeons & cosmetic clinics

Industry/Entity Type

Marketing

Contact Information for Business Card

Darren Okoye
Online Marketing Strategist

Darren@VelvetPixelPromotions.example
0491 268 517

LinkedIn: in/darrenokoye

```html
<!DOCTYPE html>
<html lang="en">
<head>
<meta charset="utf-8">
<title>Velvet Pixel Promotions — Business Card</title>
<link href="https://fonts.googleapis.com/css2?family=Questrial&family=Arimo:wght@700&display=swap" rel="stylesheet">
<style>
  :root {
    --page: #ffffff;
    --silver-dark: #b4b4b4;
    --silver-mid: #d6d6d6;
    --silver-light: #f4f4f4;
    --ring: rgba(255, 255, 255, 0.72);
    --ink: #2b2b2b;
    --ink-soft: #3a3a3a;
    --brand-grey: #6d6e71;
    --brand-blue: #1ba7dc;
    --icon-blue: #2b9fd9;
  }
  * { margin: 0; padding: 0; box-sizing: border-box; }
  html, body {
    width: 1041px; height: 1200px; overflow: hidden;
    background: var(--page);
  }
  .canvas { position: relative; width: 1041px; height: 1200px; }
  .card {
    position: absolute; width: 717px; height: 435px; overflow: hidden;
    background: linear-gradient(115deg, var(--silver-dark) 0%, var(--silver-light) 28%, var(--silver-mid) 44%, #fbfbfb 60%, var(--silver-mid) 82%, var(--silver-dark) 100%);
    box-shadow: 4px 6px 10px rgba(0,0,0,0.12);
  }
  .card--front { left: 146px; top: 118px; }
  .card--back { left: 149px; top: 625px; }
  .card__ring { position: absolute; inset: 0; }

  .brand {
    position: absolute; left: 117px; top: 150px;
    display: flex; align-items: center; gap: 40px;
  }
  .brand__dot {
    width: 110px; height: 110px; border-radius: 50%;
    background: var(--brand-blue);
  }
  .brand__name {
    font-family: "Questrial", sans-serif; color: var(--brand-grey);
    font-size: 46px; line-height: 46px; letter-spacing: 5px;
    text-transform: uppercase;
  }

  .contact {
    position: absolute; inset: 0; text-align: center;
    font-family: "Questrial", sans-serif; color: var(--ink-soft);
  }
  .contact__name {
    position: absolute; left: 0; right: 0; top: 104px;
    font-family: "Arimo", sans-serif; font-weight: 700;
    font-size: 24px; color: var(--ink);
  }
  .contact__role {
    position: absolute; left: 0; right: 0; top: 144px; font-size: 20px;
  }
  .contact__line {
    position: absolute; left: 0; right: 0;
    display: flex; justify-content: center; align-items: center; gap: 8px;
    font-size: 23px;
  }
  .contact__line--phone {
    top: 214px; font-family: "Arimo", sans-serif; font-weight: 700;
    font-size: 22px; color: var(--ink);
  }
  .contact__line--email { top: 265px; }
  .contact__line--social { top: 315px; }
  .icon { flex: none; }
  .icon--square {
    width: 24px; height: 24px; border-radius: 3px; background: var(--icon-blue);
  }
</style>
</head>
<body>
<div class="canvas">
  <section class="card card--front">
    <svg class="card__ring" width="717" height="435" viewBox="0 0 717 435">
      <rect x="30" y="27" width="655" height="381" rx="190" fill="none" stroke="var(--ring)" stroke-width="52"/>
    </svg>
    <div class="brand">
      <span class="brand__dot"></span>
      <p class="brand__name">Velvet<br>Pixel<br>Promotions</p>
    </div>
  </section>

  <section class="card card--back">
    <svg class="card__ring" width="717" height="435" viewBox="0 0 717 435">
      <rect x="30" y="27" width="655" height="381" rx="190" fill="none" stroke="var(--ring)" stroke-width="52"/>
    </svg>
    <div class="contact">
      <h1 class="contact__name">DARREN OKOYE</h1>
      <p class="contact__role">Online Marketing Strategist</p>
      <p class="contact__line contact__line--phone">
        <svg class="icon" width="16" height="24" viewBox="0 0 16 24">
          <path d="M5 2 C2 3 1 6 1 11 C1 16 3 20 6 22 L9 19 L6 15 C5 13 5 10 6 8 L9 5 Z" fill="var(--icon-blue)"/>
        </svg>
        0491 268 517
      </p>
      <p class="contact__line contact__line--email">
        <svg class="icon" width="26" height="18" viewBox="0 0 26 18">
          <rect x="1" y="1" width="24" height="16" fill="none" stroke="var(--icon-blue)" stroke-width="2"/>
          <path d="M1 1 L13 10 L25 1 M1 17 L10 8 M25 17 L16 8" fill="none" stroke="var(--icon-blue)" stroke-width="2"/>
        </svg>
        Darren@VelvetPixelPromotions.example
      </p>
      <p class="contact__line contact__line--social">
        <span class="icon icon--square"></span>
        in/darrenokoye
      </p>
    </div>
  </section>
</div>
</body>
</html>
```